Lodging Refresh Partners - Tabletop Display

We need a 5'x5' trade show display for a hotel renovation company named "Lodging Refresh Partners." Lodging Refresh Partners is the most complete authority on hotel renovation in the country, and we're the only 100% turn-key renovator in Colorado. With one phone call, we deliver an approved design, FF&E purchasing, logistics, construction, installation, and warranty administration. The design needs to convey professionalism. Our goal is to help our clients reduce costs and reduce stress while achieving the best results. The colors should align with the attached brochure for our Raleigh office.

Target Market(s)

Hotel owners and general managers

Industry/Entity Type

Design Agency

Colors
3277b5
85acd3
cfdeed

Requirements
Must have
• Our product is a blend of design and construction. I need to convey our services and attention to detail without seeming salesy, bold, or aggressive. The goal is to convey confidence and help to relax our potential client base.
Nice to have
• Possibly one or more photos of completed projects. Not sure if exterior, lobby, or guest room photos would be best. I can send files via dropbox if that's helpful.
Should not have
• I've included a photo of the old display at a trade show. I strongly dislike the yellow and red on the display. Please try to stick to the color palette of the attached brochure.

```html
<!DOCTYPE html>
<html lang="en">
<head>
<meta charset="utf-8">
<title>Lodging Refresh Partners – Turn-Key Renovations</title>
<link rel="stylesheet" href="https://fonts.googleapis.com/css2?family=Fira+Sans:wght@600;700&family=Raleway:wght@300&display=swap">
<style>
  :root {
    --brand-blue: #2f75b5;
    --brand-blue-deep: #1f5fa0;
    --headline-blue: #2a6fb0;
    --band-black: #1c1c1c;
    --band-grey: #6f6f6f;
    --paper: #ffffff;
    --frame: #f4f4f4;
  }
  html, body {
    margin: 0;
    padding: 0;
    overflow: hidden;
    background: var(--paper);
  }
  .display {
    position: relative;
    width: 1200px;
    height: 1200px;
    overflow: hidden;
    background: var(--paper);
    font-family: "Fira Sans", Arial, sans-serif;
  }
  .backdrop {
    position: absolute;
    inset: 0;
  }
  .brand {
    position: absolute;
    left: 52px;
    top: 120px;
    display: flex;
    align-items: flex-start;
    gap: 14px;
  }
  .brand-square {
    width: 22px;
    height: 22px;
    background: var(--brand-blue);
    margin-top: 8px;
  }
  .brand-name {
    margin: 0;
    font-family: "Fira Sans", Arial, sans-serif;
    font-weight: 700;
    font-size: 38px;
    line-height: 1.1;
    color: var(--brand-blue);
  }
  .headline {
    position: absolute;
    left: 566px;
    top: 58px;
    margin: 0;
    color: var(--headline-blue);
  }
  .headline-kicker {
    display: block;
    font-family: "Fira Sans", Arial, sans-serif;
    font-weight: 700;
    font-size: 56px;
    letter-spacing: 1px;
    line-height: 1;
  }
  .headline-main {
    display: block;
    margin-top: 14px;
    font-family: "Raleway", Arial, sans-serif;
    font-weight: 300;
    font-size: 86px;
    line-height: 1;
    letter-spacing: 1px;
  }
  .tagline-box {
    position: absolute;
    left: 468px;
    top: 869px;
    width: 732px;
    height: 97px;
    background: var(--paper);
    display: flex;
    align-items: center;
  }
  .tagline {
    margin: 0 0 0 58px;
    font-family: "Raleway", Arial, sans-serif;
    font-weight: 300;
    font-size: 64px;
    color: var(--headline-blue);
    letter-spacing: 1px;
  }
  .services {
    position: absolute;
    left: 497px;
    top: 1000px;
    margin: 0;
    padding: 0;
    list-style: none;
    display: grid;
    grid-template-columns: 268px auto;
    grid-auto-flow: column;
    grid-template-rows: repeat(4, 47px);
    color: var(--paper);
    font-weight: 600;
    font-size: 32px;
  }
  .services li {
    display: flex;
    align-items: center;
    gap: 18px;
  }
  .services li::before {
    content: "";
    width: 18px;
    height: 18px;
    background: var(--paper);
    clip-path: polygon(100% 0, 100% 100%, 0 100%);
  }
  .inset-frame {
    position: absolute;
    left: 64px;
    top: 821px;
    width: 326px;
    height: 326px;
    background: var(--frame);
    box-shadow: 0 1px 3px rgba(0,0,0,0.25);
  }
  .inset-photo {
    position: absolute;
    left: 11px;
    top: 12px;
    width: 305px;
    height: 304px;
    background: linear-gradient(160deg, #b08a68 0%, #c9b59a 45%, #8d7e6c 100%);
  }
</style>
</head>
<body>
<main class="display">
  <svg class="backdrop" width="1200" height="1200" viewBox="0 0 1200 1200" aria-hidden="false">
    <defs>
      <linearGradient id="exteriorTones" x1="0" y1="0" x2="0" y2="1">
        <stop offset="0" stop-color="#a9b8da"/>
        <stop offset="0.4" stop-color="#c89a6c"/>
        <stop offset="0.8" stop-color="#a4603a"/>
        <stop offset="1" stop-color="#6f5a46"/>
      </linearGradient>
    </defs>
    <rect class="service-band" x="0" y="982" width="1200" height="218" fill="var(--brand-blue)"/>
    <polygon class="exterior-photo" role="img" aria-label="Photo of a renovated hotel exterior at dusk with a covered entrance"
             points="428,243 1200,243 1200,982 0,982 0,984" fill="url(#exteriorTones)"/>
    <polygon class="accent-grey" points="493,130 558,243 428,243" fill="var(--band-grey)"/>
    <polygon class="accent-black" points="417,130 493,130 0,982 0,850" fill="var(--band-black)"/>
  </svg>

  <div class="brand">
    <span class="brand-square"></span>
    <p class="brand-name">Lodging<br>Refresh<br>Partners</p>
  </div>

  <h1 class="headline">
    <span class="headline-kicker">TURN-KEY</span>
    <span class="headline-main">RENOVATIONS</span>
  </h1>

  <div class="tagline-box">
    <p class="tagline">Everything Included!</p>
  </div>

  <div class="inset-frame">
    <div class="inset-photo" role="img" aria-label="Photo of a renovated guest room with a bed, sofa and coffee table"></div>
  </div>

  <ul class="services">
    <li>Design</li>
    <li>FF&amp;E</li>
    <li>Purchasing</li>
    <li>Logistics</li>
    <li>Construction</li>
    <li>Installation</li>
    <li>Warranty administration</li>
  </ul>
</main>
</body>
</html>
```